Electrical company business card design.

Hi, were an electrical company in Auckland New Zealand called Quarneth Ltd. We focus mainly on high end residential and commercial so the card would be targeted towards that.
The card will be for myself, i am the director of the company.
Name: Derek Olstow
Position: Director/electrician
Phone: 021 387 9415
Email: derek@quarneth.co.nz
Location: Auckland
As for colors the the blue color in the logo is preferred, i also don't mind a black background option.
Target Market(s)
High end residential and commercial
Industry/Entity Type
Electrician
Contact Information for Business Card
Name: Derek Olstow Position: Director/Electrician Phone: 021 387 9415, Email: derek@quarneth.co.nz, Location: Auckland

```html
<!DOCTYPE html>
<html lang="en">
<head>
<meta charset="utf-8">
<title>Derek Olstow – Business Card</title>
<link rel="stylesheet" href="https://fonts.googleapis.com/css2?family=Lexend:wght@500;600&display=swap">
<style>
  :root {
    --backdrop: #e6e6e6;
    --card-white: #ffffff;
    --card-black: #000000;
    --brand-blue: #0077c0;
  }
  * { box-sizing: border-box; margin: 0; padding: 0; }
  html, body {
    width: 1200px;
    height: 1194px;
    overflow: hidden;
    background: var(--backdrop);
    font-family: "Lexend", sans-serif;
  }
  .card {
    position: absolute;
    left: 332px;
    width: 574px;
    height: 330px;
    overflow: hidden;
  }
  .card--front { top: 207px; background: var(--card-white); }
  .card--back { top: 613px; background: var(--card-black); }

  .front__name {
    position: absolute;
    top: 138px;
    left: 0;
    width: 100%;
    text-align: center;
    color: var(--brand-blue);
    font-weight: 600;
    font-size: 42px;
    letter-spacing: 1px;
    text-transform: uppercase;
    line-height: 1;
  }
  .front__stripe {
    position: absolute;
    left: 0;
    top: 289px;
    width: 574px;
    height: 16px;
  }

  .back__art {
    position: absolute;
    inset: 0;
    width: 574px;
    height: 330px;
  }
  .back__divider {
    position: absolute;
    left: 319px;
    top: 49px;
    width: 3px;
    height: 234px;
    background: var(--brand-blue);
  }
  .back__details {
    position: absolute;
    left: 348px;
    top: 74px;
    color: var(--brand-blue);
    font-weight: 500;
  }
  .back__role {
    font-size: 15.5px;
    letter-spacing: 0.4px;
    padding-bottom: 8px;
    width: 216px;
    border-bottom: 3px solid var(--brand-blue);
  }
  .back__phone {
    display: flex;
    align-items: center;
    gap: 13px;
    margin-top: 35px;
    font-size: 19px;
    font-weight: 600;
  }
  .back__phone svg { width: 16px; height: 16px; }
  .back__location {
    margin-top: 27px;
    font-size: 14px;
    letter-spacing: 1.5px;
  }
</style>
</head>
<body>
  <section class="card card--front">
    <p class="front__name">Derek Olstow</p>
    <svg class="front__stripe" viewBox="0 0 574 16" aria-hidden="true">
      <polygon points="0,0 120,0 104,16 0,16" fill="var(--card-black)"/>
      <polygon points="143,0 574,0 574,16 126,16" fill="var(--card-black)"/>
    </svg>
  </section>

  <section class="card card--back">
    <svg class="back__art" viewBox="0 0 574 330" aria-hidden="true">
      <circle cx="446" cy="165" r="304" fill="none" stroke="var(--card-white)" stroke-width="20"/>
      <circle cx="153" cy="165" r="130" fill="var(--card-black)"/>
      <circle cx="153" cy="165" r="118" fill="var(--card-white)"/>
    </svg>
    <div class="back__divider"></div>
    <div class="back__details">
      <p class="back__role">DIRECTOR/ELECTRICIAN</p>
      <p class="back__phone">
        <svg viewBox="0 0 24 24" aria-hidden="true"><path fill="var(--brand-blue)" d="M6.6 10.8c1.4 2.8 3.8 5.1 6.6 6.6l2.2-2.2c.3-.3.7-.4 1-.2 1.1.4 2.3.6 3.6.6.6 0 1 .4 1 1V20c0 .6-.4 1-1 1C10.6 21 3 13.4 3 4c0-.6.4-1 1-1h3.5c.6 0 1 .4 1 1 0 1.3.2 2.5.6 3.6.1.3 0 .7-.2 1z"/></svg>
        021 387 9415
      </p>
      <p class="back__location">LOCATION: AUCKLAND</p>
    </div>
  </section>
</body>
</html>
```